METAL FABRICATION BUSINESS CARD

** I will be ending the project and picking design early. This Friday October 3rd at 7am MST if not sooner**
ONE SIDED BUSINESS CARD ONLY. AND LOGO SIZE TO BE DOMINANT so it stands out.
Looking for a black background and will be doing raised chrome/silver font on the business cards. Looking to have the following on the front of the business card. Company logo is uploaded in files.
Company logo
*Compartment Doors
*Roof Radius Metal
*J-Wrap Metal Skirting
*S-Lock Beltline Molding
*Pre-Bent Molding
and more...
Owen Baskell 406.529.1847 info@Trelvo-Works.com
Updates
One sided business card only please. Also logo size should be dominant and sized bigger
Contact Information for Business Card
Black background, Text will be raised chrome/silver, and corners will be rounded.

```html
<!DOCTYPE html>
<html lang="en">
<head>
<meta charset="utf-8">
<title>Trelvo Works Business Card</title>
<link rel="stylesheet" href="https://fonts.googleapis.com/css2?family=Montserrat:wght@400;500;600;700&display=swap">
<style>
  :root {
    --backdrop: #999999;
    --card-black: #161616;
    --chrome: #d9d9d9;
    --chrome-soft: #e6e6e6;
    --chrome-dim: #bdbdbd;
  }
  * { box-sizing: border-box; margin: 0; padding: 0; }
  html, body {
    width: 1200px;
    height: 1108px;
    overflow: hidden;
    background: var(--backdrop);
    font-family: "Montserrat", Arial, sans-serif;
  }
  .canvas { position: relative; width: 1200px; height: 1108px; }
  .card {
    position: absolute;
    left: 242px;
    width: 715px;
    height: 409px;
    border-radius: 30px;
    background: var(--card-black);
    color: var(--chrome);
  }
  .card--front { top: 119px; }
  .card--back { top: 580px; }

  .brand {
    position: absolute;
    display: flex;
    align-items: center;
    font-weight: 700;
    color: var(--chrome);
    white-space: nowrap;
    letter-spacing: 0.5px;
  }
  .brand__dot {
    border-radius: 50%;
    background: var(--chrome);
    flex: none;
  }
  .card--front .brand {
    left: 0; right: 0; top: 160px;
    justify-content: center;
    font-size: 66px;
    gap: 18px;
  }
  .card--front .brand__dot { width: 34px; height: 34px; }
  .card--back .brand {
    left: 28px; top: 60px;
    font-size: 46px;
    gap: 13px;
  }
  .card--back .brand__dot { width: 24px; height: 24px; }

  .services {
    position: absolute;
    right: 28px;
    top: 170px;
    text-align: right;
  }
  .services__title {
    font-size: 41px;
    font-weight: 700;
    color: var(--chrome-dim);
    letter-spacing: 0.5px;
    margin-bottom: 16px;
  }
  .services__list { list-style: none; }
  .services__item {
    font-size: 18px;
    font-weight: 500;
    color: var(--chrome-soft);
    line-height: 31px;
    letter-spacing: 0.6px;
  }

  .contact { position: absolute; left: 29px; top: 255px; }
  .contact__name {
    font-size: 32px;
    font-weight: 600;
    color: var(--chrome);
    margin-bottom: 34px;
  }
  .contact__line {
    display: flex;
    align-items: center;
    gap: 10px;
    font-size: 18px;
    color: var(--chrome-soft);
    line-height: 32px;
    letter-spacing: 0.4px;
  }
  .contact__icon { width: 16px; height: 16px; flex: none; fill: var(--chrome-soft); }
</style>
</head>
<body>
<div class="canvas">
  <section class="card card--front">
    <div class="brand"><span class="brand__dot"></span>Trelvo Works</div>
  </section>

  <section class="card card--back">
    <div class="brand"><span class="brand__dot"></span>Trelvo Works</div>

    <div class="services">
      <h2 class="services__title">OUR SERVICE</h2>
      <ul class="services__list">
        <li class="services__item">Compartment Doors</li>
        <li class="services__item">*Roof Radius Metal</li>
        <li class="services__item">*J-Wrap Metal Skirting</li>
        <li class="services__item">*S-Lock Beltline Molding</li>
        <li class="services__item">*Pre-Bent Molding</li>
      </ul>
    </div>

    <div class="contact">
      <p class="contact__name">Owen Baskell</p>
      <p class="contact__line">
        <svg class="contact__icon" viewBox="0 0 16 16" aria-hidden="true"><path d="M1 6c0-2 3-3.5 7-3.5S15 4 15 6v1.3h-3.4V5.6H4.4v1.7H1z"/><path d="M4 8.5h8l1.5 4.5H2.5z"/></svg>
        406.529.1847
      </p>
      <p class="contact__line">
        <svg class="contact__icon" viewBox="0 0 16 16" aria-hidden="true"><path d="M1 4h14v9H1z M2 5l6 4.5L14 5" fill="none" stroke="#e6e6e6" stroke-width="1.4"/></svg>
        info@Trelvo-Works.com
      </p>
    </div>
  </section>
</div>
</body>
</html>
```